Poster for homelessness project (2 day deadline)

Amber Lantern Scheme is an initiative in the UK which aims to ensure that people who are new to sleeping on the street are quickly given assistance to take them out of situation they find themselves in.

It began as a London-based project but is now being rolled out nationwide. I am working for a project based in the north of England.

We need some posters which show an image of a place where a rough sleeper may spend the night with some supporting graphic design.

I have three initial images, but I need to be able to easily swap out the images for others. I would appreciate if you could produce three posters for me, each with a different image.

-
Please note:
My client is quite vague about what they want at the moment and the above words may change. I need the selected product to be a layered raw file that I can amend myself with any Adobe CS5.5 (or below) application.

Any typefaces that you choose need to be easily purchasable online.

Please view formatinfo.pdf for formatting guidelines.

Target Market(s)

The general public. It will be placed in public places.

Industry/Entity Type

Graphic Design

Requirements
Must have
• Must contain the words:

"Tonight someone will sleep rough for the first time. Help us make sure they find the Amber Lantern."

"Would you sleep here? Sleeping rough is dangerous. Make sure everyone finds the Amber Lantern."

-
Nice to have
• I'd like this to be quite bleak, grimy and "urban" in feel.

You may recolour/tint the images in any way to enhance this feeling.

```html
<!DOCTYPE html>
<html lang="en">
<head>
<meta charset="utf-8">
<title>Amber Lantern Scheme – Tonight Someone Will Sleep Rough</title>
<link rel="stylesheet" href="https://fonts.googleapis.com/css2?family=Rubik+Dirt&family=Poiret+One&family=Nothing+You+Could+Do&family=Oswald:wght@300;400&display=swap">
<style>
  :root {
    --ochre-glow: #e2b45a;
    --amber-light: #d49a34;
    --amber: #c07418;
    --rust: #8e3a10;
    --brick: #7a2410;
    --blood: #551509;
    --soot: #24100a;
    --paper: #f6ecd8;
  }
  * { margin: 0; padding: 0; box-sizing: border-box; }
  html, body {
    width: 850px;
    height: 1200px;
    overflow: hidden;
    background: var(--soot);
  }
  .poster {
    position: relative;
    width: 850px;
    height: 1200px;
    overflow: hidden;
    color: var(--paper);
  }
  .scene-photo {
    position: absolute;
    inset: 0;
    background:
      radial-gradient(ellipse 220px 380px at 560px 420px, rgba(236, 196, 120, 0.55) 0%, rgba(236, 196, 120, 0) 100%),
      radial-gradient(ellipse 260px 160px at 760px 150px, rgba(70, 28, 8, 0.55) 0%, rgba(70, 28, 8, 0) 100%),
      radial-gradient(ellipse 520px 420px at 720px 900px, rgba(85, 21, 9, 0.95) 0%, rgba(122, 36, 16, 0.6) 55%, rgba(122, 36, 16, 0) 100%),
      radial-gradient(ellipse 260px 260px at 60px 720px, rgba(36, 16, 10, 0.75) 0%, rgba(36, 16, 10, 0) 100%),
      linear-gradient(160deg, rgba(36, 16, 10, 0) 55%, rgba(60, 18, 8, 0.55) 75%, rgba(36, 16, 10, 0.85) 100%),
      linear-gradient(90deg, rgba(90, 40, 10, 0.45) 0%, rgba(90, 40, 10, 0) 35%, rgba(90, 40, 10, 0) 80%, rgba(90, 40, 10, 0.4) 100%),
      linear-gradient(180deg, var(--amber) 0%, var(--amber-light) 25%, var(--ochre-glow) 45%, var(--rust) 72%, var(--brick) 86%, var(--blood) 100%);
  }
  .headline {
    position: absolute;
    top: -12px;
    left: 0;
    width: 850px;
    text-align: center;
    font-family: "Rubik Dirt", "Impact", sans-serif;
    font-size: 172px;
    line-height: 1;
    letter-spacing: 2px;
    text-transform: uppercase;
  }
  .subject {
    position: absolute;
    top: 208px;
    left: 34px;
    font-family: "Poiret One", sans-serif;
    font-size: 100px;
    line-height: 1;
    text-transform: uppercase;
    letter-spacing: 4px;
  }
  .statement {
    position: absolute;
    top: 362px;
    left: 38px;
    font-family: "Nothing You Could Do", cursive;
    font-size: 36px;
    line-height: 1.2;
    letter-spacing: 1px;
    white-space: nowrap;
  }
  .statement .stress { font-size: 52px; }
  .appeal {
    position: absolute;
    left: 40px;
    top: 938px;
    font-family: "Oswald", sans-serif;
    font-weight: 300;
  }
  .appeal-lead {
    font-size: 62px;
    line-height: 1;
    letter-spacing: -1px;
  }
  .appeal-main {
    font-size: 108px;
    line-height: 1;
    font-weight: 400;
    letter-spacing: -2px;
    white-space: nowrap;
  }
  .appeal-main .appeal-tail {
    font-size: 42px;
    font-weight: 300;
    letter-spacing: 0;
  }
  .footer-line {
    position: absolute;
    left: 0;
    bottom: 24px;
    width: 850px;
    text-align: center;
    font-family: "Oswald", sans-serif;
    font-weight: 300;
    font-size: 19px;
    letter-spacing: 0.2px;
  }
</style>
</head>
<body>
  <main class="poster">
    <div class="scene-photo" role="img" aria-label="Grimy, amber-tinted photograph of a corrugated metal wall with a wooden bench in the foreground, a place where a rough sleeper might spend the night"></div>

    <h1 class="headline">Tonight</h1>
    <p class="subject">Someone</p>
    <p class="statement">will sleep rough for the <span class="stress">first</span> time.</p>

    <div class="appeal">
      <p class="appeal-lead">Help us make sure</p>
      <p class="appeal-main">they find <span class="appeal-tail">the Amber Lantern</span></p>
    </div>

    <p class="footer-line">Would you sleep here? Sleeping rough is dangerous. Make sure everyone finds the Amber Lantern.</p>
  </main>
</body>
</html>
```